Business Cards for a law firm

Business cards for our law firm. Use our silhoette logo and OAK HARBOR - check our website (www.oakharbor-legal.com)

Contact Information for Business Card

our silhouette logo, OAK HARBOR, 800-555-0147, Dorian Kestrup, dorian@oakharbor-legal.com

Requirements
Must have
• our silhouette logo, OAK HARBOR, 800-555-0147, Dorian Kestrup, dorian@oakharbor-legal.com

```html
<!DOCTYPE html>
<html lang="en">
<head>
<meta charset="utf-8">
<title>Oak Harbor Business Cards</title>
<link rel="stylesheet" href="https://fonts.googleapis.com/css2?family=Cinzel:wght@400;700&display=swap">
<style>
  :root {
    --backdrop: #d2d3d5;
    --card: #ffffff;
    --ink: #22306b;
  }
  * { margin: 0; padding: 0; box-sizing: border-box; }
  html, body {
    width: 900px;
    height: 1200px;
    overflow: hidden;
    background: var(--backdrop);
  }
  body {
    position: relative;
    font-family: "Cinzel", "Copperplate", serif;
    color: var(--ink);
  }
  .card {
    position: absolute;
    left: 134px;
    width: 632px;
    height: 364px;
    background: var(--card);
  }
  .card--front { top: 210px; }
  .card--back { top: 624px; }

  .front-brand {
    position: absolute;
    left: 60px;
    top: 170px;
    display: flex;
    align-items: center;
    gap: 22px;
  }
  .brand-mark {
    width: 30px;
    height: 30px;
    background: var(--ink);
  }
  .brand-name {
    font-weight: 700;
    font-size: 47px;
    line-height: 1;
    letter-spacing: 1px;
  }
  .front-url {
    position: absolute;
    left: 0;
    right: 0;
    top: 317px;
    text-align: center;
    font-weight: 700;
    font-size: 12px;
    letter-spacing: 3.5px;
  }

  .back-brand {
    position: absolute;
    left: 40px;
    top: 46px;
    font-weight: 700;
    font-size: 28px;
    letter-spacing: 0.5px;
    line-height: 1;
  }
  .person {
    position: absolute;
    left: 40px;
    top: 184px;
  }
  .person-name {
    font-weight: 700;
    font-size: 25px;
    line-height: 1;
    letter-spacing: 0.5px;
  }
  .person-role {
    margin-top: 6px;
    font-size: 14px;
    letter-spacing: 0.3px;
  }
  .contact-list {
    list-style: none;
    margin-top: 14px;
  }
  .contact-item {
    display: flex;
    align-items: center;
    gap: 6px;
    height: 26px;
    font-size: 12.5px;
    letter-spacing: 0.3px;
  }
  .contact-item--phone {
    font-size: 15px;
    letter-spacing: 2px;
  }
  .contact-icon {
    width: 14px;
    height: 14px;
    fill: var(--ink);
    flex: none;
  }
</style>
</head>
<body>
  <section class="card card--front">
    <div class="front-brand">
      <span class="brand-mark"></span>
      <span class="brand-name">OAK HARBOR</span>
    </div>
    <p class="front-url">WWW.OAKHARBOR-LEGAL.COM</p>
  </section>

  <section class="card card--back">
    <p class="back-brand">OAK HARBOR</p>
    <div class="person">
      <p class="person-name">DORIAN KESTRUP</p>
      <p class="person-role">ATTORNEY</p>
      <ul class="contact-list">
        <li class="contact-item contact-item--phone">
          <svg class="contact-icon" viewBox="0 0 24 24" aria-hidden="true"><path d="M6.6 10.8a15.1 15.1 0 0 0 6.6 6.6l2.2-2.2a1 1 0 0 1 1-.25 11.4 11.4 0 0 0 3.6.57 1 1 0 0 1 1 1V20a1 1 0 0 1-1 1A17 17 0 0 1 3 4a1 1 0 0 1 1-1h3.5a1 1 0 0 1 1 1c0 1.25.2 2.45.57 3.57a1 1 0 0 1-.25 1z"/></svg>
          800-555-0147
        </li>
        <li class="contact-item">
          <svg class="contact-icon" viewBox="0 0 24 24" aria-hidden="true"><path d="M2 5h20v14H2z M3.5 6.5 12 13l8.5-6.5" fill="none" stroke="#22306b" stroke-width="0"/><path d="M2 5h20v1.5L12 13 2 6.5zM2 8.5l6.5 4.3L2 18zM22 8.5l-6.5 4.3L22 18zM10 14l2 1.3 2-1.3 7.5 5H2.5z"/></svg>
          DORIAN@OAKHARBOR-LEGAL.COM
        </li>
        <li class="contact-item">
          <svg class="contact-icon" viewBox="0 0 24 24" aria-hidden="true"><circle cx="12" cy="12" r="9.5" fill="none" stroke="#22306b" stroke-width="2"/><ellipse cx="12" cy="12" rx="4" ry="9.5" fill="none" stroke="#22306b" stroke-width="1.6"/><path d="M2.5 12h19M4 7h16M4 17h16" stroke="#22306b" stroke-width="1.6"/></svg>
          WWW.OAKHARBOR-LEGAL.COM
        </li>
      </ul>
    </div>
  </section>
</body>
</html>
```